Commercial Real Estate

We need a business card design for a new commercial real estate business that specializes in apartment building brokerage. Not individual units but the entire complex. We find and represent the owners existing buildings and well as new buyers for those buildings. The design should convey trust, integrity, knowledge and growth. It should be easily read.

Target Market(s)

40 to 65 years old

Industry/Entity Type

Real Estate

```html
<!DOCTYPE html>
<html lang="en">
<head>
<meta charset="utf-8">
<title>Tallwick Property Investments – Business Card</title>
<link href="https://fonts.googleapis.com/css2?family=Open+Sans:wght@400&family=Questrial&display=swap" rel="stylesheet">
<style>
  :root {
    --card-bg: #ffffff;
    --brand-teal: #66d3cf;
    --ink-slate: #3b5052;
    --band-text: #ffffff;
  }
  html, body {
    margin: 0;
    padding: 0;
    width: 1200px;
    height: 720px;
    overflow: hidden;
    background: var(--card-bg);
  }
  .card {
    position: relative;
    width: 1200px;
    height: 720px;
    background: var(--card-bg);
    color: var(--ink-slate);
    font-family: "Questrial", "Century Gothic", sans-serif;
  }
  .brand {
    position: absolute;
    top: 120px;
    left: 0;
    width: 1200px;
    display: flex;
    flex-direction: column;
    align-items: center;
  }
  .brand-square {
    width: 72px;
    height: 72px;
    background: var(--brand-teal);
    margin-bottom: 64px;
  }
  .brand-name {
    font-size: 38px;
    letter-spacing: 3px;
    line-height: 1;
    text-transform: uppercase;
    margin: 0;
  }
  .brand-sub {
    font-size: 16px;
    letter-spacing: 2.5px;
    line-height: 1;
    margin: 12px 0 0;
  }
  .tagline-band {
    position: absolute;
    top: 391px;
    left: 0;
    width: 1200px;
    height: 86px;
    background: var(--brand-teal);
    display: flex;
    align-items: center;
    justify-content: center;
  }
  .tagline {
    margin: 0;
    font-family: "Open Sans", "Segoe UI", sans-serif;
    font-size: 42px;
    letter-spacing: 2.2px;
    white-space: nowrap;
    color: var(--band-text);
  }
  .person p, .contact p { margin: 0; white-space: nowrap; }
  .person {
    position: absolute;
    left: 40px;
    top: 542px;
    font-size: 52px;
    line-height: 48px;
  }
  .contact {
    position: absolute;
    right: 40px;
    top: 542px;
    text-align: right;
    font-size: 52px;
    line-height: 49px;
    letter-spacing: 0.5px;
  }
</style>
</head>
<body>
  <main class="card">
    <header class="brand">
      <div class="brand-square"></div>
      <p class="brand-name">Tallwick</p>
      <p class="brand-sub">Property Investments</p>
    </header>

    <section class="tagline-band">
      <p class="tagline">Specializing in Apartment Building Brokerage.</p>
    </section>

    <section class="person">
      <p class="person-name">Your Name</p>
      <p class="person-title">Title</p>
    </section>

    <section class="contact">
      <p class="contact-phone">555.310.4827</p>
      <p class="contact-email">your email@email.com</p>
      <p class="contact-web">www.email.com</p>
    </section>
  </main>
</body>
</html>
```